Business Card Update, need to bring life to the card, two sided color

We need a new business card design, are moving and changing addresses and need a new look, we have the logos already attached but need a new style moving forward. Can incorporate the color of the logo (The Green) as well, maybe a solid back? We deal with safety products revolving around static electricity and safety lighting. Would like to keep same font in second logo as well.

Target Market(s)

Electrical Safety, Lighting

Contact Information for Business Card

Lars Whitcombe
Vice President
Office: 555-284-7316
Cell: 555-862-0457
lars@tkwhitcombe.com
www.tkwhitcombe.com
4700 West Cedar Boulevard
Suite #320
Roswell, GA 30412

Font styles to use
Serif
Sans Serif

Requirements
Must have
• Since 1918
Nice to have
• Could use the 100 Year Logo for back of card, would like the back of card to be the same green as logo.
Should not have
• No black cards please.

```html
<!DOCTYPE html>
<html lang="en">
<head>
<meta charset="utf-8">
<title>T.K. Whitcombe – Business Card</title>
<link rel="stylesheet" href="https://fonts.googleapis.com/css2?family=Open+Sans:wght@300;400;700&display=swap">
<style>
  :root {
    --brand-green: #12985a;
    --brand-green-faint: #4fb985;
    --card-white: #f7f7f5;
    --stage: #e4e6e5;
    --text-white: #ffffff;
  }
  * { box-sizing: border-box; margin: 0; padding: 0; }
  html, body {
    width: 1200px; height: 900px; overflow: hidden;
    background: var(--stage);
    font-family: "Open Sans", Arial, sans-serif;
  }
  .sheet {
    width: 1200px; height: 900px;
    display: flex; align-items: center; justify-content: center; gap: 48px;
  }
  .card {
    position: relative;
    width: 540px; height: 309px;
    overflow: hidden;
    box-shadow: 0 6px 18px rgba(0,0,0,.18);
  }
  .card-front { background: var(--card-white); }
  .card-back { background: var(--brand-green); }
  .front-swoosh { position: absolute; inset: 0; }

  .holder { position: absolute; left: 30px; top: 26px; }
  .holder-name { color: var(--brand-green); font-weight: 700; font-size: 26px; line-height: 1.15; white-space: nowrap; }
  .holder-title { color: var(--brand-green); font-weight: 400; font-size: 15px; margin-top: 2px; white-space: nowrap; }

  .brand-mark {
    position: absolute; display: flex; align-items: center; gap: 10px;
    color: var(--brand-green); font-weight: 700; font-size: 16px;
    white-space: nowrap;
  }
  .brand-mark .dot {
    flex: none;
    width: 28px; height: 28px; border-radius: 50%;
    border: 3px solid var(--brand-green);
  }
  .front-mark { right: 30px; top: 34px; }

  .contact {
    position: absolute; left: 30px; bottom: 18px;
    color: var(--text-white); font-weight: 300; font-size: 12.5px; line-height: 1.55;
    list-style: none;
  }
  .contact li { display: flex; align-items: center; gap: 8px; white-space: nowrap; }
  .contact svg { width: 12px; height: 12px; flex: none; }
  .contact-label { font-weight: 400; }

  .address {
    position: absolute; right: 30px; bottom: 18px; text-align: right;
    color: var(--text-white); font-weight: 300; font-size: 12.5px; line-height: 1.55;
    font-style: normal; white-space: nowrap;
  }

  .back-center {
    position: absolute; left: 50%; top: 50%; transform: translate(-50%, -50%);
    display: flex; flex-direction: column; align-items: center; gap: 12px;
  }
  .back-mark {
    position: static;
    color: var(--brand-green-faint); font-size: 32px; gap: 16px;
  }
  .back-mark .dot { width: 50px; height: 50px; border-color: var(--brand-green-faint); border-width: 5px; }
  .since {
    color: var(--text-white); font-weight: 400; font-size: 15px;
    letter-spacing: .3em; text-transform: uppercase; white-space: nowrap;
  }
</style>
</head>
<body>
<main class="sheet">

  <section class="card card-front" aria-label="Card front">
    <svg class="front-swoosh" viewBox="0 0 540 309" width="540" height="309" aria-hidden="true">
      <path d="M0 196 C 170 196 360 160 540 146 L540 309 L0 309 Z" fill="var(--brand-green)"/>
      <path d="M0 172 C 170 168 360 130 540 118 C 360 140 170 176 0 184 Z" fill="var(--brand-green)"/>
      <path d="M0 150 C 170 144 360 108 540 98 C 360 116 170 150 0 156 Z" fill="var(--brand-green)"/>
    </svg>

    <div class="holder">
      <p class="holder-name">Lars Whitcombe</p>
      <p class="holder-title">Vice President</p>
    </div>

    <div class="brand-mark front-mark">
      <span class="dot"></span>
      <span class="brand-name">T.K. Whitcombe</span>
    </div>

    <ul class="contact">
      <li>
        <svg viewBox="0 0 16 16" aria-hidden="true"><path d="M4 1.5l2.2 3-1.4 1.6a9 9 0 0 0 5.1 5.1l1.6-1.4 3 2.2-1.3 2.3C7.5 14.5 1.5 8.5 1.7 2.8z" fill="#fff"/></svg>
        <span><span class="contact-label">Office:</span> 555-284-7316</span>
      </li>
      <li>
        <svg viewBox="0 0 16 16" aria-hidden="true"><rect x="4" y="1" width="8" height="14" rx="1.5" fill="#fff"/><rect x="5.5" y="3" width="5" height="8" fill="var(--brand-green)"/></svg>
        <span><span class="contact-label">Cell:</span> 555-862-0457</span>
      </li>
      <li>
        <svg viewBox="0 0 16 16" aria-hidden="true"><rect x="1" y="3" width="14" height="10" fill="#fff"/><path d="M1.5 3.5 8 9l6.5-5.5" stroke="var(--brand-green)" stroke-width="1.4" fill="none"/></svg>
        <span>lars@tkwhitcombe.com</span>
      </li>
      <li>
        <svg viewBox="0 0 16 16" aria-hidden="true"><circle cx="8" cy="8" r="6.5" fill="none" stroke="#fff" stroke-width="1.5"/><path d="M1.5 8h13M8 1.5c-3 3.5-3 9.5 0 13M8 1.5c3 3.5 3 9.5 0 13" stroke="#fff" stroke-width="1.2" fill="none"/></svg>
        <span>www.tkwhitcombe.com</span>
      </li>
    </ul>

    <address class="address">
      <p>4700 West Cedar Boulevard</p>
      <p>Suite #320</p>
      <p>Roswell, GA 30412</p>
    </address>
  </section>

  <section class="card card-back" aria-label="Card back">
    <div class="back-center">
      <div class="brand-mark back-mark">
        <span class="dot"></span>
        <span class="brand-name">T.K. Whitcombe</span>
      </div>
      <p class="since">Since 1918</p>
    </div>
  </section>

</main>
</body>
</html>
```